Award-winnning Estate Agent needs a premium version of their 'For Sale' board design

We need a premium option for our 'For Sale' board design. We have a standard board that is attached to this brief, but were are looking to have a premium design version that we will use when selling exclusive properties. Our company name is Harbour Lane Estates and the name for this is exclusive selection is: 'The Harbour Collection'. The design needs to work with our current brand, but have a distinctive PREMIUM feel to it. I have uploaded the barnd guidelines and also some of the exisisting logo variations. We do NOT need a new logo but feel free to play around with colours, fonts, sizes etc. for the sign.

Target Market(s)

Property buyers & house hunters

Industry/Entity Type

Real Estate - Residential Property

Font styles to use
Sans Serif

Requirements
Must have
• A premium fee, must be square design, must be easy to read when driving past the sign
Nice to have
• I'm open ot ideas

```html
<!DOCTYPE html>
<html lang="en">
<head>
<meta charset="utf-8">
<title>Harbour Lane Estates – The Harbour Collection For Sale Board</title>
<link rel="stylesheet" href="https://fonts.googleapis.com/css2?family=Inter:wght@500&family=Montserrat:wght@400;700&display=swap">
<style>
  :root {
    --page-bg: #dcdde0;
    --board-top: #4068a9;
    --board-mid: #34499a;
    --board-bottom: #2b368a;
    --accent-stripe: #4f9bd6;
    --side-strip: #ffffff;
    --phone-band: #3e2f7c;
    --pattern-tone: #2e3b90;
    --frame-line: rgba(120, 150, 220, 0.45);
    --text-light: #ffffff;
    --text-soft: #d6e2f5;
    --text-navy: #2b2f8c;
  }
  * { margin: 0; padding: 0; box-sizing: border-box; }
  html, body {
    width: 900px; height: 1200px; overflow: hidden;
    background: var(--page-bg);
  }
  .canvas { position: relative; width: 900px; height: 1200px; }
  .board {
    position: absolute; left: 60px; top: 210px;
    width: 780px; height: 780px;
    box-shadow: 4px 4px 10px rgba(0,0,0,0.18);
  }
  .board-main {
    position: absolute; left: 0; top: 0; width: 658px; height: 100%;
    background: linear-gradient(180deg, var(--board-top) 0%, var(--board-mid) 45%, var(--board-bottom) 100%);
  }
  .accent-stripe {
    position: absolute; left: 658px; top: 0; width: 13px; height: 100%;
    background: var(--accent-stripe);
  }
  .side-strip {
    position: absolute; left: 671px; top: 0; width: 109px; height: 100%;
    background: var(--side-strip);
  }
  .web-address {
    position: absolute; left: 0; top: 0; width: 109px; height: 100%;
    display: flex; align-items: center; justify-content: center;
    writing-mode: vertical-rl; transform: rotate(180deg);
    font-family: "Montserrat", sans-serif; font-weight: 400;
    font-size: 33px; letter-spacing: 0.5px;
    color: var(--text-navy); white-space: nowrap;
  }
  .brand-row {
    position: absolute; left: 0; top: 36px; width: 658px; height: 60px;
    display: flex; align-items: center; justify-content: center; gap: 18px;
  }
  .brand-mark {
    width: 46px; height: 46px; background: var(--text-light);
  }
  .brand-name {
    font-family: "Inter", sans-serif; font-weight: 500;
    font-size: 44px; letter-spacing: -0.5px;
    color: var(--text-light); white-space: nowrap;
  }
  .collection-name {
    position: absolute; left: 0; top: 110px; width: 658px;
    text-align: center;
    font-family: "Montserrat", sans-serif; font-weight: 400;
    font-size: 22px; letter-spacing: 5px; text-transform: uppercase;
    color: var(--text-soft);
  }
  .headline-frame {
    position: absolute; left: 33px; top: 160px; width: 580px; height: 300px;
    border: 1px solid var(--frame-line);
  }
  .headline {
    position: absolute; left: 70px; top: 170px;
    font-family: "Montserrat", sans-serif; font-weight: 700;
    font-size: 150px; line-height: 138px;
    color: var(--text-light); letter-spacing: -2px;
  }
  .ornament-area {
    position: absolute; left: 130px; top: 484px; width: 400px; height: 76px;
    background: radial-gradient(ellipse at 50% 100%, rgba(80,110,190,0.35), rgba(80,110,190,0) 70%);
  }
  .phone-band {
    position: absolute; left: 0; top: 560px; width: 658px; height: 120px;
    background: var(--phone-band);
    box-shadow: 0 4px 8px rgba(0,0,0,0.25);
    display: flex; align-items: center; justify-content: center;
    font-family: "Montserrat", sans-serif; font-weight: 700;
    font-size: 72px; letter-spacing: 1px;
    color: var(--text-light);
  }
  .pattern-area {
    position: absolute; left: 0; top: 680px; width: 658px; height: 100px;
    background: linear-gradient(180deg, var(--pattern-tone), var(--board-bottom));
  }
</style>
</head>
<body>
<div class="canvas">
  <div class="board">
    <div class="board-main">
      <div class="brand-row">
        <div class="brand-mark"></div>
        <div class="brand-name">Harbour Lane Estates</div>
      </div>
      <div class="collection-name">The Harbour Collection</div>
      <div class="headline-frame"></div>
      <div class="headline">FOR<br>SALE</div>
      <div class="ornament-area" role="img" aria-label="Faint decorative scroll flourish"></div>
      <div class="pattern-area" role="img" aria-label="Subtle tone-on-tone swirl pattern"></div>
      <div class="phone-band">01632 960418</div>
    </div>
    <div class="accent-stripe"></div>
    <div class="side-strip">
      <div class="web-address">WWW.HARBOURLANEESTATES.CO.UK</div>
    </div>
  </div>
</div>
</body>
</html>
```